Redesign our current website with a more professional feel

We currently have a running website that generates some traffic and looks ok but now we want to revamp it with professional eye catching design.
We are open to proposals and open to any new ideas or suggestions but we have to see your previous work.
our current site is www.brelk-solutions.com.au

Thank you for your time and we look forward to seeing your proposals

Target Market(s)

Business owners, managers

Industry/Entity Type

Security

Number of Pages Required

5+ page

```html
<!DOCTYPE html>
<html lang="en">
<head>
<meta charset="utf-8">
<title>Brelk Solutions – Quality Security Service</title>
<link rel="stylesheet" href="https://fonts.googleapis.com/css2?family=Oswald:wght@400;500;600&family=Open+Sans:wght@400;600&display=swap">
<style>
  :root {
    --navy: #1d2a6e;
    --red: #8e1f1f;
    --ink: #333638;
    --muted: #6b6e72;
    --band: #f1f1f1;
    --rule: #d9d9d9;
    --white: #ffffff;
    --icon-grey: #9a9ea3;
  }
  * { box-sizing: border-box; margin: 0; padding: 0; }
  html, body { width: 707px; height: 1200px; overflow: hidden; background: var(--white); }
  body { font-family: "Open Sans", Arial, sans-serif; color: var(--ink); position: relative; }

  .hero { position: relative; height: 318px; overflow: hidden; }
  .hero-photo {
    position: absolute; inset: 0;
    background: linear-gradient(100deg, #8c9094 0%, #c9cbcc 30%, #e4e4e2 52%, #a9abab 72%, #5b5f63 100%);
  }
  .site-header {
    position: absolute; top: 0; left: 0; right: 0; height: 54px;
    display: flex; align-items: center; justify-content: space-between; padding: 0 28px 0 40px;
  }
  .brand { display: flex; align-items: center; gap: 8px; text-decoration: none; }
  .brand-square { width: 14px; height: 14px; background: var(--navy); }
  .brand-name { font-family: "Oswald", sans-serif; font-weight: 500; font-size: 17px; color: var(--white); letter-spacing: .5px; }
  .main-nav { display: flex; gap: 16px; }
  .main-nav a { font-family: "Oswald", sans-serif; font-size: 10.5px; color: var(--white); text-decoration: none; letter-spacing: .3px; }
  .hero-title {
    position: absolute; left: 50%; top: 140px; transform: translateX(-50%);
    border: 3px solid var(--white); padding: 6px 22px;
    font-family: "Oswald", sans-serif; font-weight: 500; font-size: 34px; color: var(--white);
    letter-spacing: 1px; white-space: nowrap; text-shadow: 0 1px 3px rgba(0,0,0,.25);
  }
  .slider-dots { position: absolute; left: 0; right: 0; top: 302px; display: flex; justify-content: center; gap: 5px; }
  .slider-dots span { width: 5px; height: 5px; border-radius: 50%; background: rgba(255,255,255,.55); }
  .slider-dots span.active { background: var(--white); }

  .boxed-title {
    display: block; margin: 0 auto; width: 212px; height: 48px;
    border: 4px solid var(--navy); text-align: center;
    font-family: "Oswald", sans-serif; font-weight: 500; font-size: 15px; color: var(--navy);
    line-height: 40px; letter-spacing: .6px;
  }

  .strengths { position: absolute; top: 360px; left: 0; right: 0; }
  .columns { display: grid; grid-template-columns: repeat(3, 1fr); gap: 22px; padding: 0 50px; margin-top: 30px; }
  .column h3 { font-family: "Oswald", sans-serif; font-weight: 500; font-size: 13px; color: var(--navy); text-align: center; letter-spacing: .4px; margin-bottom: 6px; }
  .column p { font-size: 8.6px; line-height: 1.45; color: var(--ink); }

  .testimonial { position: absolute; top: 600px; left: 0; right: 0; height: 132px; background: var(--band); text-align: center; padding-top: 14px; }
  .testimonial h2 { font-family: "Oswald", sans-serif; font-weight: 500; font-size: 12.5px; color: var(--navy); letter-spacing: .4px; }
  .testimonial h2::after { content: ""; display: block; width: 360px; height: 1px; background: var(--rule); margin: 7px auto 0; }
  .quote { position: relative; width: 300px; margin: 10px auto 0; font-size: 9.5px; line-height: 1.5; text-align: left; }
  .quote svg { position: absolute; top: 0; width: 16px; height: 14px; }
  .quote .q-open { left: -24px; }
  .quote .q-close { right: -24px; }
  .quote-author { margin-top: 10px; font-size: 8px; line-height: 1.45; color: var(--muted); text-align: right; padding-right: 190px; }
  .quote-author span { display: block; }

  .offers { position: absolute; top: 772px; left: 0; right: 0; }
  .offer-grid { display: grid; grid-template-columns: repeat(3, 193px); gap: 22px; justify-content: center; margin-top: 40px; }
  .offer-price { height: 50px; background: var(--red); color: var(--white); font-family: "Oswald", sans-serif; font-weight: 500; font-size: 14.5px; display: flex; align-items: center; justify-content: center; letter-spacing: .3px; }
  .offer h3 { font-family: "Oswald", sans-serif; font-weight: 500; font-size: 13px; color: var(--navy); margin: 14px 0 5px; letter-spacing: .3px; }
  .offer p { font-size: 8.6px; line-height: 1.45; }
  .conditions { text-align: center; font-size: 8px; color: var(--muted); margin-top: 22px; }

  .call-band { position: absolute; top: 1046px; left: 0; right: 0; height: 76px; background: var(--navy); color: var(--white); text-align: center; padding-top: 14px; }
  .call-band p { font-family: "Oswald", sans-serif; font-size: 10px; letter-spacing: .8px; }
  .call-band .phone { display: inline-flex; align-items: center; gap: 8px; font-family: "Oswald", sans-serif; font-weight: 500; font-size: 22px; margin-top: 4px; }
  .call-band svg { width: 20px; height: 20px; }

  .site-footer { position: absolute; top: 1122px; left: 0; right: 0; height: 78px; display: flex; align-items: center; justify-content: space-between; padding: 0 28px 0 22px; }
  .site-footer address { font-style: normal; font-size: 7.5px; color: var(--muted); }
  .social { display: flex; gap: 12px; }
  .social span { width: 12px; height: 12px; border-radius: 50%; background: var(--icon-grey); }
</style>
</head>
<body>

<section class="hero">
  <div class="hero-photo" role="img" aria-label="Photo of a bright modern office lobby with lifts, a large door number and a person walking through"></div>
  <header class="site-header">
    <a class="brand" href="#"><span class="brand-square"></span><span class="brand-name">Brelk Solutions</span></a>
    <nav class="main-nav">
      <a href="#">About Us</a>
      <a href="#">Services</a>
      <a href="#">Case Studies</a>
      <a href="#">Special Offers</a>
    </nav>
  </header>
  <h1 class="hero-title">QUALITY SECURITY SERVICE</h1>
  <div class="slider-dots"><span></span><span class="active"></span><span></span><span></span></div>
</section>

<section class="strengths">
  <h2 class="boxed-title">THE BEST IN AUSTRALIA</h2>
  <div class="columns">
    <article class="column">
      <h3>RESPONSIBLE</h3>
      <p>Lorem ipsum dolor sit amet, consectetur adipiscing elit, sed do eiusmod tempor incididunt ut labore et dolore magna aliqua. Ut enim ad minim veniam, quis nostrud exercitation ullamco laboris nisi ut aliquip ex ea commodo consequat.</p>
    </article>
    <article class="column">
      <h3>RELIABLE</h3>
      <p>Lorem ipsum dolor sit amet, consectetur adipiscing elit, sed do eiusmod tempor incididunt ut labore et dolore magna aliqua. Ut enim ad minim veniam, quis nostrud exercitation ullamco laboris nisi ut aliquip ex ea commodo consequat.</p>
    </article>
    <article class="column">
      <h3>TRUSTWORTHY</h3>
      <p>Lorem ipsum dolor sit amet, consectetur adipiscing elit, sed do eiusmod tempor incididunt ut labore et dolore magna aliqua. Ut enim ad minim veniam, quis nostrud exercitation ullamco laboris nisi ut aliquip ex ea commodo consequat.</p>
    </article>
  </div>
</section>

<section class="testimonial">
  <h2>WHAT OUR CUSTOMERS SAY</h2>
  <blockquote class="quote">
    <svg class="q-open" viewBox="0 0 16 14"><path fill="#b5b8bb" d="M0 14V8C0 3 2.5.5 7 0v3C4.5 3.5 3.5 5 3.5 7H7v7zm9 0V8c0-5 2.5-7.5 7-8v3c-2.5.5-3.5 2-3.5 4H16v7z"/></svg>
    Brelk Solutions have a very capable and hard working team who always meet or exceed client expectations.
    <svg class="q-close" viewBox="0 0 16 14"><path fill="#b5b8bb" d="M16 0v6c0 5-2.5 7.5-7 8v-3c2.5-.5 3.5-2 3.5-4H9V0zM7 0v6c0 5-2.5 7.5-7 8v-3c2.5-.5 3.5-2 3.5-4H0V0z"/></svg>
  </blockquote>
  <p class="quote-author"><span>Daniel Hart</span><span>(Senior Environmental Engineer, formerly at Corvane Labs)</span></p>
</section>

<section class="offers">
  <h2 class="boxed-title">SPECIAL OFFERS</h2>
  <div class="offer-grid">
    <article class="offer">
      <div class="offer-price">$40 per month installed *</div>
      <h3>BUSINESS INTRUDER ALARM</h3>
      <p>Professional B-zone alarm panel.<br>For your safety and security.</p>
    </article>
    <article class="offer">
      <div class="offer-price">3 Months FREE</div>
      <h3>NEW INSTALLATIONS</h3>
      <p>Back to base alarm monitoring with all new installations.</p>
    </article>
    <article class="offer">
      <div class="offer-price">$80 per month installed *</div>
      <h3>CCTV PACKAGE</h3>
      <p>CCTV that can be viewed from home, office or your mobile.</p>
    </article>
  </div>
  <p class="conditions">*conditions apply</p>
</section>

<section class="call-band">
  <p>GET SECURED TODAY</p>
  <div class="phone">
    <svg viewBox="0 0 24 24"><path fill="#ffffff" d="M6.6 10.8a15.1 15.1 0 0 0 6.6 6.6l2.2-2.2c.3-.3.7-.4 1-.2 1.1.4 2.3.6 3.6.6.6 0 1 .4 1 1V20c0 .6-.4 1-1 1A17 17 0 0 1 3 4c0-.6.4-1 1-1h3.5c.6 0 1 .4 1 1 0 1.3.2 2.5.6 3.6.1.3 0 .7-.2 1z"/></svg>
    1300 22 4819
  </div>
</section>

<footer class="site-footer">
  <address>Suite 4/ 18 Marlow Street, Kelby, 2150 | Phone: 1300 22 4819 | Email: info@brelk-solutions.com.au</address>
  <div class="social"><span></span><span></span><span></span></div>
</footer>

</body>
</html>
```